Business Card Design Project

In addition to the logo design we want a professional and contemporary business card for a talent management agency. We provide management services to creative artists and want to communicate a professional creative vibe.
Updates

Project Deadline Extended
Reason: Sorry didnt realise I had put such a short timeline on it.

Target Market(s)

The business deals with creative artists and other industry professionals

Industry/Entity Type

Artists

Colors

Designer to choose colors to be used in the design.

Requirements
Must have
• Logo
Address
Phone
Email

```html
<!DOCTYPE html>
<html lang="en">
<head>
<meta charset="utf-8">
<title>Velora Artists – Business Cards</title>
<link rel="stylesheet" href="https://fonts.googleapis.com/css2?family=Exo+2:wght@500&family=Tinos&display=swap">
<style>
  :root {
    --ink: #141518;
    --ink-soft: #1d1f23;
    --paper: #f4f4f4;
    --mute: #a4a6aa;
    --stage: #e6e6e6;
  }
  * { margin: 0; padding: 0; box-sizing: border-box; }
  html, body { width: 1200px; height: 1000px; overflow: hidden; }
  body { background: var(--stage); position: relative; }

  .card {
    position: absolute;
    width: 560px;
    height: 320px;
    overflow: hidden;
    box-shadow: 0 10px 28px rgba(0,0,0,.18);
  }
  .card--front { left: 90px; top: 120px; background: var(--paper); }
  .card--back  { left: 550px; top: 560px; background: var(--ink); }

  .panel { position: absolute; inset: 0; }
  .card--front .panel {
    background: linear-gradient(160deg, var(--ink-soft), var(--ink));
    clip-path: polygon(330px 0, 560px 0, 560px 300px, 400px 110px, 330px 110px);
  }
  .card--back .panel {
    background: var(--paper);
    clip-path: polygon(300px 0, 560px 0, 560px 150px, 430px 100px, 370px 110px);
  }

  .wordmark {
    position: absolute;
    font-family: "Exo 2", sans-serif;
    font-weight: 500;
    line-height: 1;
    letter-spacing: 2px;
  }
  .wordmark__name { display: block; font-size: 46px; letter-spacing: 3px; }
  .wordmark__sub  { display: block; font-size: 30px; margin-top: 4px; padding-left: 34px; }
  .card--front .wordmark { left: 70px; top: 120px; color: var(--ink); }
  .card--back  .wordmark { left: 60px; top: 110px; color: var(--paper); }

  .web {
    position: absolute;
    left: 104px; top: 232px;
    font-family: "Exo 2", sans-serif;
    font-size: 12px;
    letter-spacing: 4px;
    color: #555;
  }

  .address {
    position: absolute;
    right: 22px; top: 18px;
    display: flex; gap: 8px; align-items: flex-start;
    font-family: "Tinos", serif;
    font-size: 12px;
    line-height: 1.4;
    color: var(--ink);
    text-align: right;
  }
  .address svg { width: 10px; height: 14px; margin-top: 2px; }

  .contacts {
    position: absolute;
    left: 60px; bottom: 34px;
    list-style: none;
    font-family: "Tinos", serif;
    font-size: 13px;
    color: var(--mute);
    letter-spacing: .5px;
  }
  .contacts li { display: flex; align-items: center; gap: 12px; height: 24px; }
  .contacts svg { width: 16px; height: 14px; fill: none; stroke: var(--mute); stroke-width: 1.4; }
</style>
</head>
<body>

  <section class="card card--front" aria-label="Business card front">
    <div class="panel"></div>
    <div class="wordmark">
      <span class="wordmark__name">VELORA</span>
      <span class="wordmark__sub">Artists</span>
    </div>
    <p class="web">WWW.VELORA.COM.AU</p>
  </section>

  <section class="card card--back" aria-label="Business card back">
    <div class="panel"></div>
    <div class="address">
      <p>14-18 Kent Street Redfern NSW 2016<br>Australia</p>
      <svg viewBox="0 0 10 14" aria-hidden="true"><path d="M5 0C2 0 0 2.3 0 5c0 3.5 5 9 5 9s5-5.5 5-9C10 2.3 8 0 5 0z" fill="#141518"/><circle cx="5" cy="5" r="1.8" fill="#f4f4f4"/></svg>
    </div>
    <div class="wordmark">
      <span class="wordmark__name">VELORA</span>
      <span class="wordmark__sub">Artists</span>
    </div>
    <ul class="contacts">
      <li>
        <svg viewBox="0 0 16 14" aria-hidden="true"><path d="M2 3h12v9H2z M5 3c0-1.5 6-1.5 6 0"/><circle cx="8" cy="8" r="2"/></svg>
        (+61 2) 9400 1234
      </li>
      <li>
        <svg viewBox="0 0 16 14" aria-hidden="true"><path d="M1 2h14v10H1z M1 2l7 6 7-6"/></svg>
        hello@veloramail.com
      </li>
      <li>
        <svg viewBox="0 0 16 14" aria-hidden="true"><path d="M1 1h14v9H1z M6 13h4 M8 10v3"/></svg>
        www.velora.com.au
      </li>
    </ul>
  </section>

</body>
</html>
```